Brightmoor Partners Branding Revamp

We are a consulting company, looking for a way to display and promote our brand. We have 2 sides to the business- Brightmoor (financial) and Partners (cyber security). The financial side products relate to business necessities: card processing, website design/hosting/maintenance, VoIP phone systems. The cyber security side promotes a bundled package of 4 solutions: network vulnerability scan, dark web scan, anti-ransomeware/malware software, and image-level backups. We want people to understand that partnering with Brightmoor Partners gives them “Elevated Peace of Mind” (tagline). Current badge and logos uploaded.

Target Market(s)

Small businesses

Contact Information for Business Card

Lena Marwick, Vice President, lena@brightmoorpartners.example, 555-806-1937, www.brightmoorpartners.example

Requirements
Nice to have
• I do prefer the darker background for front and back

```html
<!DOCTYPE html>
<html lang="en">
<head>
<meta charset="utf-8">
<title>Brightmoor Partners — Business Card</title>
<link rel="stylesheet" href="https://fonts.googleapis.com/css2?family=Montserrat:wght@300;400;500&display=swap">
<style>
  :root {
    --backdrop: #1c1e21;
    --card-black: #121213;
    --red-bright: #d6141c;
    --red-mid: #a80f16;
    --red-deep: #6c0609;
    --red-line: #c8141b;
    --white: #f4f4f4;
    --muted: #bdbdbd;
  }
  * { box-sizing: border-box; margin: 0; padding: 0; }
  html, body {
    width: 1200px;
    height: 900px;
    overflow: hidden;
    background: var(--backdrop);
    font-family: "Montserrat", Arial, sans-serif;
  }
  .sheet {
    position: relative;
    width: 1200px;
    height: 900px;
  }
  .card {
    position: absolute;
    left: 250px;
    width: 700px;
    height: 400px;
    background: var(--card-black);
    overflow: hidden;
    box-shadow: 0 10px 30px rgba(0,0,0,0.45);
  }
  .card--front { top: 40px; }
  .card--back { top: 460px; }

  /* Front */
  .card__art { position: absolute; inset: 0; }
  .holder {
    position: absolute;
    left: 42px;
    top: 34px;
    color: var(--white);
  }
  .holder__name {
    font-weight: 300;
    font-size: 40px;
    letter-spacing: 0.5px;
  }
  .holder__role {
    margin-top: 6px;
    font-weight: 400;
    font-size: 11px;
    letter-spacing: 7px;
    color: var(--red-bright);
    text-transform: uppercase;
  }
  .wordmark {
    position: absolute;
    display: flex;
    align-items: center;
    gap: 14px;
  }
  .wordmark__mark {
    width: 30px;
    height: 30px;
    background: var(--red-bright);
    flex: none;
  }
  .wordmark__name {
    font-weight: 500;
    font-size: 20px;
    letter-spacing: 6px;
    line-height: 1.35;
    text-transform: uppercase;
    color: var(--white);
  }
  .card--front .wordmark { right: 44px; top: 140px; }

  .contact {
    position: absolute;
    top: 300px;
    color: var(--white);
    font-size: 13px;
    line-height: 1.55;
    font-weight: 400;
  }
  .contact--address { left: 40px; }
  .contact--phone { left: 250px; top: 308px; font-size: 14px; }
  .contact--web { left: 436px; }

  /* Back */
  .pattern { position: absolute; inset: 0; }
  .crest {
    position: absolute;
    left: 170px;
    top: 100px;
    width: 360px;
    height: 200px;
    background: var(--card-black);
    border: 2px solid var(--red-line);
    display: flex;
    flex-direction: column;
    align-items: center;
    justify-content: center;
    gap: 18px;
  }
  .crest .wordmark { position: static; }
  .crest__rule {
    width: 200px;
    height: 1px;
    background: linear-gradient(90deg, transparent, var(--red-line), transparent);
  }
  .crest__url {
    color: var(--muted);
    font-size: 10px;
    letter-spacing: 2px;
    text-transform: uppercase;
  }
</style>
</head>
<body>
<main class="sheet">

  <section class="card card--front" aria-label="Business card front">
    <svg class="card__art" width="700" height="400" viewBox="0 0 700 400" aria-hidden="true">
      <rect x="0" y="250" width="210" height="150" fill="var(--red-bright)"/>
      <rect x="210" y="250" width="210" height="150" fill="var(--red-mid)"/>
      <rect x="420" y="250" width="280" height="150" fill="var(--red-deep)"/>
      <line x1="0" y1="250" x2="700" y2="250" stroke="#000" stroke-width="3"/>
      <line x1="0" y1="384" x2="700" y2="384" stroke="#0d0d0d" stroke-width="3"/>

      <!-- icon bumps -->
      <g fill="var(--card-black)" stroke="var(--red-line)" stroke-width="2">
        <circle cx="72" cy="250" r="30"/>
        <circle cx="282" cy="250" r="30"/>
        <circle cx="620" cy="250" r="30"/>
      </g>

      <!-- pin -->
      <path d="M72 236 a10 10 0 0 1 10 10 c0 8 -10 18 -10 18 c0 0 -10 -10 -10 -18 a10 10 0 0 1 10 -10 z" fill="var(--white)"/>
      <circle cx="72" cy="246" r="3.5" fill="var(--card-black)"/>

      <!-- phone -->
      <path d="M276 238 l5 -2 l4 8 l-4 3 c1 4 3 7 6 9 l3 -3 l7 5 l-2 5 c-10 1 -21 -14 -19 -25 z" fill="var(--white)"/>

      <!-- globe -->
      <g fill="none" stroke="var(--white)" stroke-width="2.2">
        <circle cx="620" cy="250" r="13"/>
        <ellipse cx="620" cy="250" rx="6" ry="13"/>
        <line x1="607" y1="250" x2="633" y2="250"/>
        <line x1="609" y1="243" x2="631" y2="243"/>
        <line x1="609" y1="257" x2="631" y2="257"/>
      </g>
    </svg>

    <div class="holder">
      <h1 class="holder__name">Lena Marwick</h1>
      <p class="holder__role">Vice President</p>
    </div>

    <div class="wordmark">
      <span class="wordmark__mark"></span>
      <span class="wordmark__name">Brightmoor<br>Partners</span>
    </div>

    <p class="contact contact--address">47 Road Example<br>Postal, City, State</p>
    <p class="contact contact--phone">+555-806-1937</p>
    <p class="contact contact--web">lena@brightmoorpartners.example<br>www.brightmoorpartners.example</p>
  </section>

  <section class="card card--back" aria-label="Business card back">
    <svg class="pattern" width="700" height="400" viewBox="0 0 700 400" role="img" aria-label="Angular red line pattern on black background">
      <defs>
        <radialGradient id="back-glow" cx="50%" cy="50%" r="70%">
          <stop offset="0" stop-color="#2a0a0c"/>
          <stop offset="1" stop-color="#121213"/>
        </radialGradient>
      </defs>
      <rect width="700" height="400" fill="url(#back-glow)"/>
    </svg>

    <div class="crest">
      <div class="wordmark">
        <span class="wordmark__mark"></span>
        <span class="wordmark__name">Brightmoor<br>Partners</span>
      </div>
      <span class="crest__rule"></span>
      <p class="crest__url">www.brightmoorpartners.example</p>
    </div>
  </section>

</main>
</body>
</html>
```